Beer Label Design for Copper Kettle Beer Company

Hello, we are looking for a beer label design for our first bottle release, Quillburst Barleywine. We have attached a label my illustrator friend did which was rejected by the NLR because it says "Cactus Lantern" which could be confused with tequila apparently. Anyway due to a computer crash we lost the original vector file so cannot edit. Since we have a do over we are looking for new ideas. We are pretty much open to anything as long as it contains:
-Original label information
-'Velvet Harbor' 'Ale Aged in Tequila Barrels' underneath replacing 'Cactus Lantern"
-Copper Kettle Beer Company somewhere on label
-can't be obscene or it will not get approved by NLR
Attached is the original label as well as our logo and other graphics for inspiration.

Get creative and look forward to working with you.

Cheers!

Industry/Entity Type

Brewery

Requirements
Must have
• -Fit to attached template for printing (sorry forgot to attach this last night!) Necker can be used for Copper Kettle Beer Company but not a must have for design if it fits on square label.
• -Stand out in a row of bottles
• -Original label information
• -'Velvet Harbor' 'Ale Aged in Tequila Barrels' underneath replacing 'Cactus Lantern"
• -Copper Kettle Beer Company somewhere on label
• -can't be obscene or it will not get approved by NLR
Nice to have
• What is a quillburst? We have no idea either but it won the contest we held to name our anniversary beer. We like rockets, ufo's, old school planets. Our preference is vintage but are open minded.

```html
<!DOCTYPE html>
<html lang="en">
<head>
<meta charset="utf-8">
<title>Quillburst Barleywine — Label</title>
<link rel="stylesheet" href="https://fonts.googleapis.com/css2?family=Lilita+One&family=Oswald:wght@500;600&family=Kaushan+Script&family=Roboto+Condensed:wght@400;700&display=swap">
<style>
  :root {
    --label-red: #e01e1e;
    --art-red: #c9191a;
    --shadow-red: #8e1010;
    --ink: #0b0b0b;
    --paper: #ffffff;
  }
  * { margin: 0; padding: 0; box-sizing: border-box; }
  html, body { width: 1200px; height: 839px; overflow: hidden; background: var(--paper); }
  .label { position: relative; width: 1200px; height: 839px; }

  .info-panel {
    position: absolute; left: 656px; top: 178px; width: 380px; height: 486px;
    background: var(--ink);
  }
  .rocket { position: absolute; left: 0; top: 0; width: 1200px; height: 839px; }

  .brand-name {
    position: absolute; left: 507px; top: 116px; transform: translateX(-50%);
    font-family: "Oswald", sans-serif; font-weight: 600; font-size: 30px; line-height: 40px;
    color: var(--paper); letter-spacing: 0.5px; white-space: nowrap;
  }

  .beer-title {
    position: absolute; left: 507px; top: 470px; transform: translateX(-50%);
    font-family: "Lilita One", sans-serif; font-size: 86px; line-height: 92px;
    color: var(--paper); text-align: center; white-space: nowrap;
    text-shadow: 4px 5px 0 var(--shadow-red);
  }

  .stats {
    position: absolute; left: 712px; top: 216px; width: 80px;
    font-family: "Oswald", sans-serif; font-weight: 500; color: var(--paper);
    text-align: center; font-size: 36px; line-height: 42px;
  }
  .stats .abv { margin-bottom: 18px; }

  .vertical {
    position: absolute; transform-origin: top left; transform: rotate(-90deg);
  }
  .style-name {
    left: 798px; top: 650px; width: 460px; height: 56px; white-space: nowrap;
    font-family: "Kaushan Script", cursive; font-size: 40px; line-height: 56px;
    color: var(--label-red);
  }
  .style-desc {
    left: 856px; top: 650px; width: 460px; height: 50px; white-space: nowrap;
    font-family: "Kaushan Script", cursive; font-size: 32px; line-height: 50px;
    color: var(--paper);
  }
  .legal {
    left: 918px; top: 652px; width: 462px; height: 100px;
    font-family: "Roboto Condensed", sans-serif; font-size: 10.6px; line-height: 18.5px;
    color: var(--paper);
  }
  .legal .strong { font-weight: 700; white-space: nowrap; }
</style>
</head>
<body>
<main class="label">
  <div class="info-panel"></div>

  <svg class="rocket" viewBox="0 0 1200 839" xmlns="http://www.w3.org/2000/svg">
    <g fill="var(--label-red)" stroke="var(--ink)" stroke-width="4" stroke-linejoin="round">
      <path class="fin-left" d="M344,440 C288,432 232,500 228,600 L234,770 C238,806 282,806 290,770 L348,664 Z"/>
      <path class="fin-right" d="M670,440 C726,432 782,500 786,600 L780,770 C776,806 732,806 724,770 L666,664 Z"/>
      <rect class="fin-center" x="478" y="680" width="58" height="122" rx="29"/>
      <path class="body" d="M507,32 C610,80 684,220 690,420 L660,716 L354,716 L324,420 C330,220 404,80 507,32 Z"/>
    </g>
    <path class="illustration" role="img" aria-label="Illustration of a space pilot in a helmet, inked in black over red"
          d="M507,170 C590,205 650,300 662,420 L638,700 L376,700 L352,420 C364,300 424,205 507,170 Z"
          fill="var(--art-red)"/>
  </svg>

  <div class="brand-name">COPPER KETTLE</div>

  <h1 class="beer-title">QUILLBURST<br>BARLEYWINE</h1>

  <div class="stats">
    <div class="abv">AL<br>12,8%</div>
    <div class="volume">22<br>OZ</div>
  </div>

  <div class="vertical style-name">Velvet Harbor</div>
  <div class="vertical style-desc">Ale Aged in Tequila Barrels</div>
  <div class="vertical legal">
    <div class="strong">BREWED AND BOTTLED / PACKED BY COPPER KETTLE BEER COMPANY</div>
    <div class="strong">5120 Pine Ridge Rd Unit B Flagstaff, AZ 86001</div>
    <p>GOVERNMENT WARNING: (1) According to the Surgeon General, women should not drink alcoholic beverages during pregnancy because of the risk of birth defects. (2) Consumption of alcoholic beverages impairs your ability to drive a car or operate machinery, and may cause health problems.</p>
  </div>
</main>
</body>
</html>
```